Amber Tides: Lantern Tales from Seven Winters by the Northern Sea and Other Small Wonders

Good day! I am excited to work again with you, amazing designers! This time I am looking for the cover design of my book.
Dimensions 6” x 9”
The book name is as my name project. I love simplicity, but yet that is impactful. I love colours, I don't have a specific colour in mind, but I like the mustard colour as the one in the logo of my company. I am open to ideas! I have attached some cover samples that I like so that it gives a better idea of what I have on mind.
I am looking for something that looks professional, yet, not super serious, that it's approachable to people. Something that calls their attention at first glance.
I am working with my editor and my interior designer as well to finalize this part of the book. I will be working with the person that I select for the book design to finalize it.
About the book, here a passage of an unedited version of the introduction for guidance :
My intention is to take you on a journey to help you to understand what is going on in your mind so that you get out from anything that is holding you back in your life. My intention is to guide you to start fully living and experiencing a life that your mind even have yet conceived. To experience a life where you live fearless and without suffering. Living your life where you are the navigator and the creator of how you are experiencing it and you are living in a world of possibilities where there are no limitations.
For it, we will start to understand more about the mind and about the brain. I am not a neuroscientist and neither I consider my self an expert in the workings of the brain, what I know is the result of my fascination about our brain. This curiosity and the part of me that likes to understand how things work took me to read, research and learn about how our brain works and how its intrinsic mechanisms are subconsciously influencing and limiting us. I encourage you to stay on this part, it can be a bit technical, but understanding how it works will empower you not to allow your mind to dictate the way you approach your life and to live on autopilot.
We will continue to describe how you have been programmed throughout your life, putting you inside a box limited by your subconscious beliefs and ideas about the world. In this part, we will also discuss what ego is, how it is subconsciously limiting you and how the ways of when ego manifests itself are limiting you and making you suffer. Now that you know how you have been enclosed in your mind for all your life, we will move to discuss how you can get out of it. You will learn how to master your emotions to eliminate your suffering and not allow them to control the direction of your life and use them as a mechanism to get out from your programed mind. We continue to discuss how to leverage the power of your mind and harness your power of choice. Finally, I invite you to see yourself as a holistic being so that you start truly living and take control over the direction of your life, by nourishing and taking care of all those aspects of you utilizing their wisdom and synergy to achieve higher connection within yourself, your soul and live your life in a higher level of consciousness with peace, flow, love and purpose.

```html
<!DOCTYPE html>
<html lang="en">
<head>
<meta charset="utf-8">
<title>Amber Tides — Book Cover</title>
<link rel="stylesheet" href="https://fonts.googleapis.com/css2?family=Anton&family=Poppins:wght@300;700&display=swap">
<style>
  :root {
    --stage: #eeeeee;
    --navy-edge: #1b3c6c;
    --navy-core: #2563a6;
    --mustard: #f5bb1a;
    --paper-white: #ffffff;
    --title-white: #f2f2f2;
  }
  html, body {
    margin: 0;
    padding: 0;
    width: 1200px;
    height: 1108px;
    overflow: hidden;
    background: var(--stage);
  }
  .stage {
    position: relative;
    width: 1200px;
    height: 1108px;
  }
  .book-cover {
    position: absolute;
    left: 266px;
    top: 54px;
    width: 668px;
    height: 1000px;
    box-shadow: 0 10px 30px rgba(0,0,0,0.18);
  }
  .book-cover svg {
    display: block;
    width: 100%;
    height: 100%;
  }
  .title-main {
    font-family: "Anton", "Impact", sans-serif;
    fill: var(--title-white);
  }
  .title-accent {
    font-family: "Anton", "Impact", sans-serif;
    fill: var(--mustard);
  }
  .subtitle {
    font-family: "Poppins", sans-serif;
    font-weight: 300;
    font-size: 21px;
    fill: var(--paper-white);
  }
  .author {
    font-family: "Poppins", sans-serif;
    font-weight: 700;
    font-size: 44px;
    letter-spacing: 1px;
    fill: var(--paper-white);
  }
</style>
</head>
<body>
<div class="stage">
  <div class="book-cover">
    <svg viewBox="0 0 668 1000" xmlns="http://www.w3.org/2000/svg" aria-label="Book cover: Amber Tides by Elin Marsh">
      <defs>
        <radialGradient id="cover-glow" cx="0.42" cy="0.42" r="0.75">
          <stop offset="0" stop-color="var(--navy-core)"/>
          <stop offset="1" stop-color="var(--navy-edge)"/>
        </radialGradient>
      </defs>

      <rect class="cover-ground" x="0" y="0" width="668" height="1000" fill="url(#cover-glow)"/>

      <g class="rising-arrow" fill="var(--mustard)">
        <polygon points="329,67 405,0 481,67"/>
        <rect x="375" y="66" width="60" height="350"/>
      </g>

      <text class="title-main" x="25" y="649" font-size="330" textLength="623" lengthAdjust="spacingAndGlyphs">amber</text>
      <text class="title-accent" x="300" y="885" font-size="228" textLength="362" lengthAdjust="spacingAndGlyphs">tides</text>

      <g class="subtitle" text-anchor="end">
        <text x="285" y="745">Lantern Tales from</text>
        <text x="285" y="776">Seven Winters by the</text>
        <text x="285" y="807">Northern Sea &amp; Other</text>
        <text x="285" y="838">Small Wonders</text>
      </g>

      <rect class="author-band" x="0" y="913" width="668" height="87" fill="var(--mustard)"/>
      <text class="author" x="334" y="972" text-anchor="middle">ELIN MARSH</text>
    </svg>
  </div>
</div>
</body>
</html>
```